Landing Page - Mortgage Loan Intake

We are a mortgage company seeking a clean, easy-to-use landing page that consists of minimal copy and creative with a short intake form for customers to sign up to work with us on securing their home financing. We will soon have Kv and Tandro campaigns running throughout the US, and those ads will lead to this landing page. We need at least one landing page for now and may need a slightly different version for A/B testing,. We will expand the project at the beginning of next year with additional versions with the same branding, just geared towards slightly different loan products.

This is the existing intake form we would incorporate on our landing page:

https://apply.brevafund.com/#/create-account

Here is some of the existing content that we would use as a springboard for the design, color scheme, and content of the landing page:

https://corlinhomeloans.com/https://corlinhomeloans.com/about/https://corlinhomeloans.com/refinance/consolidate-debt/

I have also included images that are related to what we're looking for either visually (feel and format) or in terms of the message.

Target Market(s)

people (borrowers) looking for a refinance or debt consolidation through a refinance

Industry/Entity Type

Mortgage Lender

Number of Pages Required

1 page

Font styles to use
Other font styles liked:
• unsure of the name but we would use the font currently used on corlinhomeloans.com

Colors
9bcb3b
cee9f5
ffffff
85acd3
cfeae6
abd036
cadf82
cedeed

Requirements
Must have
• intake form, clean light feel
Nice to have
• explanation of debt consolidation benefits or easy process via a simple infographic or illustration with a clean layout
Should not have
• anything off-brand (colors that are too heavy or not clean and airy)

```html
<!DOCTYPE html>
<html lang="en">
<head>
<meta charset="utf-8">
<title>Corlin Mortgage – Start Your Loan Application</title>
<link rel="stylesheet" href="https://fonts.googleapis.com/css2?family=Source+Sans+3:wght@400;600;700&family=Open+Sans:wght@400;600&display=swap">
<style>
  :root {
    --page-bg: #ffffff;
    --panel-blue: #93b3d7;
    --field-grey: #cdc8c8;
    --field-text: #7a7676;
    --brand-green: #8cc63f;
    --button-green: #9bc674;
    --ink: #111111;
    --ink-soft: #4a4242;
    --link-grey: #555555;
    --white: #ffffff;
  }
  * { box-sizing: border-box; margin: 0; padding: 0; }
  html, body {
    width: 1200px; height: 758px; overflow: hidden;
    background: var(--page-bg);
  }
  .landing {
    position: relative; width: 1200px; height: 758px;
    font-family: "Source Sans 3", "Open Sans", sans-serif;
  }
  .brand {
    position: absolute; left: 172px; top: 150px;
    display: flex; align-items: center; gap: 14px;
  }
  .brand-mark {
    width: 40px; height: 40px; background: var(--brand-green);
  }
  .brand-name {
    font-family: "Source Sans 3", sans-serif;
    font-weight: 700; font-size: 46px; line-height: 1;
    color: var(--ink); letter-spacing: -0.5px;
  }
  .headline {
    position: absolute; left: 620px; width: 430px; top: 136px;
    text-align: center;
    font-family: "Open Sans", sans-serif; font-weight: 400;
    font-size: 32px; line-height: 42px; color: var(--ink);
  }
  .panel {
    position: absolute; left: 103px; top: 224px;
    width: 971px; height: 398px; background: var(--panel-blue);
  }
  .benefits {
    position: absolute; left: 53px; top: 54px; width: 460px;
    color: var(--ink-soft);
  }
  .benefit + .benefit { margin-top: 6px; }
  .benefit-title {
    font-weight: 700; font-size: 31px; line-height: 36px;
  }
  .benefit-text {
    padding-left: 30px;
    font-size: 24px; line-height: 32px; font-weight: 400;
  }
  .signup-form {
    position: absolute; left: 541px; top: 21px; width: 393px;
  }
  .field {
    position: relative; display: flex; align-items: center;
    height: 38px; background: var(--field-grey);
    margin-bottom: 24px;
  }
  .field svg {
    position: absolute; left: 14px; top: 50%; transform: translateY(-50%);
  }
  .field-input {
    width: 100%; height: 100%; border: 0; background: transparent;
    padding-left: 59px;
    font-family: "Open Sans", sans-serif; font-size: 15px; color: var(--field-text);
  }
  .field-input::placeholder { color: var(--field-text); }
  .create-button {
    display: block; width: 100%; height: 37px; margin-top: -1px;
    border: 0; border-radius: 10px; background: var(--button-green);
    color: var(--white);
    font-family: "Open Sans", sans-serif; font-weight: 600;
    font-size: 16px; letter-spacing: 0.3px; word-spacing: 3px;
  }
  .signin-note {
    margin-top: 5px; text-align: center;
    font-family: "Open Sans", sans-serif; font-weight: 600;
    font-size: 11px; color: #2f2f2f;
  }
  .signin-note a { color: var(--link-grey); margin-left: 4px; }
</style>
</head>
<body>
<main class="landing">
  <div class="brand">
    <span class="brand-mark"></span>
    <span class="brand-name">Corlin Mortgage</span>
  </div>

  <h1 class="headline">Let's get started<br>on your loan application</h1>

  <section class="panel">
    <div class="benefits">
      <div class="benefit">
        <h2 class="benefit-title">Secure</h2>
        <p class="benefit-text">Your data is protected with industry standard encryption.</p>
      </div>
      <div class="benefit">
        <h2 class="benefit-title">Autosaved</h2>
        <p class="benefit-text">We’ll save your information as you go.</p>
      </div>
      <div class="benefit">
        <h2 class="benefit-title">Less paperwork</h2>
        <p class="benefit-text">Import income and asset information directly to your application.</p>
      </div>
    </div>

    <form class="signup-form">
      <label class="field">
        <svg width="16" height="30" viewBox="0 0 16 30" aria-hidden="true">
          <path d="M8 2 C3 2 3 10 8 13 C13 10 13 2 8 2 Z M8 13 L3 28 M8 13 L13 28" fill="none" stroke="var(--brand-green)" stroke-width="2.6" stroke-linecap="round"/>
        </svg>
        <input class="field-input" type="text" placeholder="Name">
      </label>
      <label class="field">
        <svg width="26" height="18" viewBox="0 0 26 18" aria-hidden="true">
          <rect x="0" y="0" width="26" height="18" fill="var(--brand-green)"/>
          <path d="M1 1 L13 10 L25 1 M1 17 L10 8 M25 17 L16 8" fill="none" stroke="var(--field-grey)" stroke-width="1.4"/>
        </svg>
        <input class="field-input" type="email" placeholder="E-mail Address">
      </label>
      <label class="field">
        <svg width="24" height="18" viewBox="0 0 26 18" aria-hidden="true">
          <rect x="0" y="0" width="26" height="18" fill="var(--brand-green)"/>
          <path d="M1 1 L13 10 L25 1 M1 17 L10 8 M25 17 L16 8" fill="none" stroke="var(--field-grey)" stroke-width="1.4"/>
        </svg>
        <input class="field-input" type="email" placeholder="Confirm E-mail Address">
      </label>
      <label class="field">
        <svg width="22" height="30" viewBox="0 0 22 30" aria-hidden="true">
          <path d="M2 3 L7 5 L11 1 L15 5 L20 3 L20 16 C20 23 15 27 11 29 C7 27 2 23 2 16 Z" fill="var(--brand-green)"/>
        </svg>
        <input class="field-input" type="password" placeholder="Password">
      </label>
      <label class="field">
        <svg width="22" height="30" viewBox="0 0 22 30" aria-hidden="true">
          <path d="M2 3 L7 5 L11 1 L15 5 L20 3 L20 16 C20 23 15 27 11 29 C7 27 2 23 2 16 Z" fill="var(--brand-green)"/>
        </svg>
        <input class="field-input" type="password" placeholder="Confirm Password">
      </label>
      <button class="create-button" type="submit">CREATE ACCOUNT</button>
      <p class="signin-note">ALREADY HAVE AN ACCOUNT? <a href="#">SIGN IN</a></p>
    </form>
  </section>
</main>
</body>
</html>
```